Marlow Law Stationery - Letterhead, Envelopes, Business Cards

We need high quality business stationery for our Personal Injury Law Firm located in Houston, Texas. The design should include the logo, Marlow Law Group, PLLC, 713-555-4718, 2150 Fernbrook Avenue, Suite 310, Houston, Texas 77019 www.MarlowLaw.example. The colors are blue and white. The letterhead should also include the Attorneys - Tessa Quill, Mitchell R. Marlow and Derek Hale.

```html
<!DOCTYPE html>
<html lang="en">
<head>
<meta charset="utf-8">
<title>Marlow Law Stationery</title>
<link rel="stylesheet" href="https://fonts.googleapis.com/css2?family=Lato:wght@400;700&family=Montserrat:wght@500;700&display=swap">
<style>
  :root {
    --navy: #001a3d;
    --navy-soft: #1c3357;
    --paper: #ffffff;
    --ink: #2b2f36;
    --ghost: #e3e6ec;
    --backdrop: #a0a0a0;
  }
  * { box-sizing: border-box; margin: 0; padding: 0; }
  html, body { width: 1200px; height: 857px; overflow: hidden; background: var(--backdrop); }
  .stage { position: relative; width: 1200px; height: 857px; font-family: "Lato", sans-serif; color: var(--ink); }
  .sheet { position: absolute; background: var(--paper); box-shadow: 0 4px 14px rgba(0,0,0,.28); overflow: hidden; }
  .band { position: absolute; left: 0; bottom: 0; display: block; }

  .brand { position: absolute; display: flex; align-items: center; gap: 6px; }
  .brand-dot { border-radius: 50%; background: var(--navy); flex: none; }
  .brand-name { font-family: "Lato", sans-serif; font-weight: 700; color: var(--navy); white-space: nowrap; }

  .ghost-mark { position: absolute; border-radius: 50%; border: 8px solid var(--ghost); display: flex; align-items: center; justify-content: center; }
  .ghost-mark .brand-name { color: var(--ghost); }

  /* business card front */
  .card-front { left: 94px; top: 299px; width: 200px; height: 114px; }
  .card-front .brand { right: 10px; top: 22px; }
  .card-front .brand-dot { width: 16px; height: 16px; }
  .card-front .brand-name { font-size: 9px; }
  .person-name { position: absolute; left: 13px; top: 56px; font-family: "Montserrat", sans-serif; font-weight: 700; font-size: 7.6px; color: var(--navy); letter-spacing: .3px; }
  .person-role { position: absolute; left: 13px; top: 67px; font-family: "Montserrat", sans-serif; font-weight: 500; font-size: 5.4px; color: var(--ink); letter-spacing: .2px; }
  .card-rule { position: absolute; left: 13px; right: 10px; top: 78px; height: .6px; background: var(--ink); }
  .card-contact { position: absolute; left: 13px; top: 82px; font-size: 5.2px; line-height: 9.5px; }
  .card-contact li { list-style: none; display: flex; align-items: center; gap: 3px; }
  .card-address { position: absolute; right: 10px; top: 84px; text-align: right; font-size: 5.2px; line-height: 6.8px; }
  .icon { fill: var(--navy); flex: none; }

  /* business card back */
  .card-back { left: 303px; top: 299px; width: 200px; height: 114px; background: var(--navy); }
  .card-back .brand { left: 50%; top: 50%; transform: translate(-50%, -56%); }
  .card-back .brand-dot { width: 14px; height: 14px; background: transparent; border: 1.5px solid var(--paper); }
  .card-back .brand-name { color: var(--paper); font-size: 13px; }

  /* envelope */
  .envelope { left: 89px; top: 496px; width: 542px; height: 235px; }
  .envelope > .brand { left: 34px; top: 58px; }
  .envelope > .brand .brand-dot { width: 24px; height: 24px; }
  .envelope > .brand .brand-name { font-size: 15px; }
  .envelope .ghost-mark { left: 336px; top: 8px; width: 200px; height: 200px; }
  .envelope .ghost-mark .brand-name { font-size: 26px; }

  /* letterhead */
  .letterhead { left: 671px; top: 133px; width: 472px; height: 667px; }
  .letterhead > .brand { left: 48px; top: 68px; }
  .letterhead > .brand .brand-dot { width: 26px; height: 26px; }
  .letterhead > .brand .brand-name { font-size: 16px; }
  .contact-block { position: absolute; left: 280px; top: 41px; padding-left: 12px; border-left: .8px solid var(--ink); font-size: 10.4px; line-height: 16px; }
  .contact-block li { list-style: none; display: flex; align-items: flex-start; gap: 7px; }
  .contact-block .icon { margin-top: 3px; }
  .letterhead .ghost-mark { left: 82px; top: 186px; width: 306px; height: 306px; border-width: 10px; }
  .letterhead .ghost-mark .brand-name { font-size: 42px; }
</style>
</head>
<body>
<main class="stage">

  <section class="sheet card-front" aria-label="Business card front">
    <div class="brand"><span class="brand-dot"></span><span class="brand-name">Marlow Law</span></div>
    <p class="person-name">ALDEN PRYCE</p>
    <p class="person-role">MANAGING DIRECTOR</p>
    <div class="card-rule"></div>
    <ul class="card-contact">
      <li><svg class="icon" width="5" height="5" viewBox="0 0 10 10"><path d="M2 0l2 2.5-1 1.3a6 6 0 0 0 3.2 3.2L7.5 6 10 8l-1.3 1.7C4.5 10 0 5.5.3 1.3z"/></svg>713-555-4718</li>
      <li><svg class="icon" width="5" height="5" viewBox="0 0 10 10"><circle cx="5" cy="5" r="4.2" fill="none" stroke="#001a3d" stroke-width="1.4"/><path d="M1 5h8M5 1v8"/></svg>www.MarlowLaw.example</li>
    </ul>
    <p class="card-address">2150 Fernbrook Avenue,<br>Suite 310, Houston, Texas 77019</p>
    <svg class="band" width="200" height="6" viewBox="0 0 200 6">
      <path d="M0 0h48l-1.5 1.5H0zM49 0h50l-1.5 1.5H47.5zM100 0h50l-1.5 1.5H98.5z" fill="var(--navy)"/>
      <path d="M0 3h147l3-3h50v6H0z" fill="var(--navy)"/>
    </svg>
  </section>

  <section class="sheet card-back" aria-label="Business card back">
    <div class="brand"><span class="brand-dot"></span><span class="brand-name">Marlow Law</span></div>
    <svg class="band" width="200" height="5" viewBox="0 0 200 5">
      <path d="M95 5l6-4h99v4z" fill="var(--navy-soft)"/>
    </svg>
  </section>

  <section class="sheet envelope" aria-label="Envelope">
    <div class="brand"><span class="brand-dot"></span><span class="brand-name">Marlow Law</span></div>
    <div class="ghost-mark"><span class="brand-name">Marlow Law</span></div>
    <svg class="band" width="542" height="17" viewBox="0 0 542 17">
      <path d="M0 1h130l-3 3.5H0zM131 1h140l-3 3.5H128zM272 1h140l-3 3.5H269z" fill="var(--navy)"/>
      <path d="M0 11h406l12-11h124v17H0z" fill="var(--navy)"/>
    </svg>
  </section>

  <section class="sheet letterhead" aria-label="Letterhead">
    <div class="brand"><span class="brand-dot"></span><span class="brand-name">Marlow Law</span></div>
    <ul class="contact-block">
      <li><svg class="icon" width="9" height="9" viewBox="0 0 10 10"><path d="M2 0l2 2.5-1 1.3a6 6 0 0 0 3.2 3.2L7.5 6 10 8l-1.3 1.7C4.5 10 0 5.5.3 1.3z"/></svg>713-555-4718</li>
      <li><svg class="icon" width="9" height="9" viewBox="0 0 10 10"><circle cx="5" cy="5" r="4.2" fill="none" stroke="#001a3d" stroke-width="1.4"/><path d="M1 5h8M5 1v8"/></svg>www.MarlowLaw.example</li>
      <li><svg class="icon" width="9" height="11" viewBox="0 0 10 12"><path d="M5 0a4.5 4.5 0 0 1 4.5 4.5C9.5 8 5 12 5 12S.5 8 .5 4.5A4.5 4.5 0 0 1 5 0zm0 2.8a1.7 1.7 0 1 0 0 3.4 1.7 1.7 0 0 0 0-3.4z"/></svg><span>2150 Fernbrook Avenue,<br>Suite 310, Houston, Texas 77019</span></li>
    </ul>
    <div class="ghost-mark"><span class="brand-name">Marlow Law</span></div>
    <svg class="band" width="472" height="15" viewBox="0 0 472 15">
      <path d="M0 0h116l-3 3H0zM117 0h122l-3 3H114zM240 0h122l-3 3H237z" fill="var(--navy)"/>
      <path d="M0 8h351l10-8h111v15H0z" fill="var(--navy)"/>
    </svg>
  </section>

</main>
</body>
</html>
```